Bluewater Products Flyer

Bluewater Lending Group, Inc.
Licensed Mortgage Company
Serving the DMV since 1997
"You choose Bluewater, we'll carry it home"
We specialize in...
FHA Loans
* Credit Scores as low as 500
* 203K Renovation Loans
Conventional Loans
* As little as 1% Down
* Bank Statement for Self-Employed
Investor Loans
* DSCR, & Fix & Flip
* Commercial & New Construction
Other Programs
* HELOCS & Reverse Mortgages
Call today for a free consultation
(800) 641-2957
www.bluewaterlendhub.com
NMLS #731846

```html
<!DOCTYPE html>
<html lang="en">
<head>
<meta charset="utf-8">
<title>Bluewater Products Flyer</title>
<link rel="stylesheet" href="https://fonts.googleapis.com/css2?family=Montserrat:wght@500;600;700;800;900&display=swap">
<style>
:root{
  --navy:#1c3657;
  --navy-deep:#142a46;
  --green:#2f9a48;
  --lime:#8dc641;
  --gold:#d8a31d;
  --mist:#e9edf1;
  --pill:#e4e7ea;
  --ink:#2b3440;
  --white:#ffffff;
}
*{margin:0;padding:0;box-sizing:border-box}
html,body{width:849px;height:1200px;overflow:hidden;background:var(--white)}
body{font-family:"Montserrat",Arial,sans-serif;color:var(--ink)}
.flyer{position:relative;width:849px;height:1200px;overflow:hidden;background:var(--white)}
.backdrop{position:absolute;inset:0}
.brand{position:absolute;left:34px;top:30px;width:230px;text-align:center}
.brand-name{display:flex;align-items:center;justify-content:center;gap:8px;font-weight:800;font-size:26px;color:var(--navy);letter-spacing:.5px}
.brand-name .dot{width:14px;height:14px;border-radius:50%;background:var(--green)}
.brand-sub{font-weight:800;font-size:15px;color:var(--navy);letter-spacing:1px;margin-top:2px}
.brand-tag{margin-top:6px;background:var(--navy);color:var(--white);font-size:7.5px;font-weight:600;padding:3px 4px;letter-spacing:.3px}
.brand-est{font-size:8px;font-weight:700;color:var(--navy);margin-top:3px;letter-spacing:1px}
.facts{position:absolute;left:18px;top:168px;width:236px;display:flex;flex-direction:column;gap:9px}
.fact{background:var(--pill);border-radius:0 24px 24px 0;padding:12px 14px;font-size:13px;font-weight:500;color:var(--ink);line-height:1.3}
.hero-photo{position:absolute;left:286px;top:-60px;width:620px;height:620px;border-radius:50%;border:8px solid var(--white);background:radial-gradient(circle at 45% 40%,#d9b48f 0%,#9a6a49 35%,#f1f1f1 70%,#dfe3e7 100%)}
.home-photo{position:absolute;left:556px;top:466px;width:170px;height:170px;border-radius:50%;border:6px solid var(--white);box-shadow:0 2px 8px rgba(0,0,0,.15);background:linear-gradient(180deg,#cfe3f1 0%,#9fb9a0 55%,#5f8a4f 100%)}
.headline{position:absolute;left:48px;top:540px;font-weight:900;font-size:60px;line-height:1.04;color:var(--navy);letter-spacing:-.5px;text-transform:uppercase}
.headline .accent{color:var(--green)}
.band{position:absolute;left:0;top:0;width:849px;height:1200px}
.products{position:absolute;left:74px;top:782px;display:flex;gap:14px}
.product{width:214px;height:214px;border-radius:50%;border:5px solid var(--white);display:flex;flex-direction:column;align-items:center;justify-content:center;text-align:center;padding:0 22px;color:var(--white)}
.product.fha{background:var(--green)}
.product.conventional{background:var(--lime);color:var(--navy-deep)}
.product.investor{background:var(--gold);color:var(--navy-deep)}
.product h2{font-size:19px;font-weight:800;line-height:1.1;text-transform:uppercase}
.product .rule{width:110px;height:2px;background:currentColor;opacity:.6;margin:8px 0}
.product p{font-size:14px;font-weight:600;line-height:1.2}
.product .big{font-size:25px;font-weight:800;line-height:1.05}
.other{position:absolute;left:52px;top:1014px;color:var(--white)}
.other h3{font-size:17px;font-weight:600;letter-spacing:.5px}
.other p{font-size:19px;font-weight:700;color:var(--lime);margin-top:2px}
.badges{position:absolute;left:560px;top:1010px;display:flex;gap:10px;align-items:center}
.badge{background:var(--white);border-radius:3px}
.badge.b1{width:42px;height:40px}
.badge.b2{width:32px;height:32px}
.badge.b3{width:70px;height:36px}
.contact{position:absolute;left:52px;top:1090px;display:flex;align-items:center;gap:14px;color:var(--white)}
.contact .line1{font-size:15px;font-weight:500}
.contact .line2{font-size:26px;font-weight:700;letter-spacing:.5px}
.web{position:absolute;left:470px;top:1100px;display:flex;align-items:center;gap:10px;color:var(--white);font-size:17px;font-weight:500}
.nmls{position:absolute;left:560px;top:1134px;color:var(--white);font-size:14px;font-weight:600}
</style>
</head>
<body>
<main class="flyer">
  <svg class="backdrop" width="849" height="1200" viewBox="0 0 849 1200" aria-hidden="true">
    <path d="M0 400 C200 470 300 500 520 470 C700 445 790 500 849 540 L849 760 C700 700 560 760 380 740 C200 720 90 680 0 650 Z" fill="var(--mist)"/>
    <path d="M0 440 C250 520 380 540 560 520 C720 500 800 560 849 600" fill="none" stroke="#dfe4e9" stroke-width="14"/>
  </svg>

  <div class="hero-photo" role="img" aria-label="Smiling family of four posing together"></div>

  <header class="brand">
    <div class="brand-name"><span class="dot"></span>Bluewater</div>
    <div class="brand-sub">LENDING GROUP</div>
    <div class="brand-tag">YOU CHOOSE BLUEWATER, WE'LL CARRY IT HOME</div>
    <div class="brand-est">EST. 1997</div>
  </header>

  <ul class="facts">
    <li class="fact" style="list-style:none">Bluewater Lending Group, Inc.</li>
    <li class="fact" style="list-style:none">Licensed Mortgage Company</li>
    <li class="fact" style="list-style:none">Serving the DMV since 1997</li>
  </ul>

  <div class="home-photo" role="img" aria-label="Family standing in front of a new home with a sold sign"></div>

  <h1 class="headline">You choose<br><span class="accent">Bluewater,</span><br>we'll carry<br>it home</h1>

  <svg class="band" width="849" height="1200" viewBox="0 0 849 1200" aria-hidden="true">
    <path d="M0 960 C250 930 560 950 849 890 L849 1200 L0 1200 Z" fill="var(--navy)"/>
    <path d="M0 952 C250 922 560 942 849 882" fill="none" stroke="var(--green)" stroke-width="5"/>
  </svg>

  <section class="products">
    <article class="product fha">
      <h2>FHA Loans</h2>
      <div class="rule"></div>
      <p>Credit Scores as low as 500</p>
      <div class="rule"></div>
      <p class="big">203K</p>
      <p>Renovation Loans</p>
    </article>
    <article class="product conventional">
      <h2>Conventional<br>Loans</h2>
      <div class="rule"></div>
      <p>As little as</p>
      <p class="big">1% Down</p>
      <div class="rule"></div>
      <p style="font-size:12px">Bank Statement for Self-Employed</p>
    </article>
    <article class="product investor">
      <h2>Investor<br>Loans</h2>
      <div class="rule"></div>
      <p>DSCR, &amp; Fix &amp; Flip</p>
      <div class="rule"></div>
      <p>Commercial &amp; New Construction</p>
    </article>
  </section>

  <section class="other">
    <h3>OTHER PROGRAMS</h3>
    <p>HELOCS &amp; Reverse Mortgages</p>
  </section>

  <div class="badges" aria-hidden="true">
    <div class="badge b1"></div>
    <div class="badge b2"></div>
    <div class="badge b3"></div>
  </div>

  <div class="contact">
    <svg width="38" height="38" viewBox="0 0 24 24" aria-hidden="true"><path fill="var(--lime)" d="M6.6 10.8a15.2 15.2 0 0 0 6.6 6.6l2.2-2.2c.3-.3.7-.4 1-.2 1.1.4 2.3.6 3.6.6.6 0 1 .4 1 1V20c0 .6-.4 1-1 1A17 17 0 0 1 3 4c0-.6.4-1 1-1h3.5c.6 0 1 .4 1 1 0 1.3.2 2.5.6 3.6.1.3 0 .7-.2 1z"/></svg>
    <div>
      <div class="line1">Call today for a free consultation</div>
      <div class="line2">(800) 641-2957</div>
    </div>
  </div>

  <div class="web">
    <svg width="22" height="22" viewBox="0 0 24 24" aria-hidden="true"><circle cx="12" cy="12" r="9" fill="none" stroke="var(--lime)" stroke-width="2"/><path d="M3 12h18M12 3c3 3 3 15 0 18M12 3c-3 3-3 15 0 18" fill="none" stroke="var(--lime)" stroke-width="1.6"/></svg>
    www.bluewaterlendhub.com
  </div>
  <div class="nmls">NMLS #731846</div>
</main>
</body>
</html>
```